Corvane Bookkeeping Services business cards

looking for a double sided business card design. My logo is attached. I am looking for a design similar to the attached. Keen to see what my logo in white on the blue background would look like.

```html
<!DOCTYPE html>
<html lang="en">
<head>
<meta charset="utf-8">
<title>Corvane Bookkeeping Services – Business Cards</title>
<link rel="stylesheet" href="https://fonts.googleapis.com/css2?family=Montserrat:wght@800&family=Roboto:wght@400;500&display=swap">
<style>
  :root {
    --stage: #2b2b2c;
    --card: #1d1e20;
    --card-edge: #26272a;
    --green: #9cc12d;
    --blue: #0c3a7a;
    --white: #f2f2f2;
    --muted: #d8d8d8;
    --faint: rgba(156, 193, 45, 0.10);
  }
  * { margin: 0; padding: 0; box-sizing: border-box; }
  html, body { width: 1200px; height: 852px; overflow: hidden; }
  body {
    background: var(--stage);
    font-family: "Roboto", Arial, sans-serif;
    position: relative;
  }
  .card {
    position: absolute;
    width: 540px;
    height: 308px;
    background: var(--card);
    border-radius: 18px;
    overflow: hidden;
    box-shadow: 0 14px 30px rgba(0,0,0,0.45);
  }
  .card--back { left: 80px; top: 120px; }
  .card--front { left: 580px; top: 424px; }

  /* back side */
  .back__url {
    position: absolute; left: 34px; top: 34px;
    color: var(--white); font-size: 15px; letter-spacing: 0.2px;
  }
  .back__mark {
    position: absolute; right: 48px; top: 30px;
    width: 170px; height: 170px;
    background: var(--card-edge); border-radius: 10px;
  }
  .wordmark {
    font-family: "Montserrat", Arial, sans-serif;
    font-weight: 800;
    line-height: 1;
  }
  .back__wordmark {
    position: absolute; left: 34px; bottom: 36px;
    color: var(--green);
  }
  .back__wordmark .wordmark__name { display: block; font-size: 52px; }
  .back__wordmark .wordmark__tag { display: block; font-size: 14.5px; letter-spacing: 1.2px; margin-top: 4px; text-transform: uppercase; }

  /* front side */
  .front__band { position: absolute; left: 0; top: 0; bottom: 0; width: 62px; background: var(--blue); }
  .front__rule { position: absolute; left: 74px; top: 0; bottom: 0; width: 6px; background: var(--green); }
  .front__mark {
    position: absolute; right: 40px; top: 28px;
    width: 120px; height: 120px; background: var(--faint); border-radius: 8px;
  }
  .front__brand {
    position: absolute; left: 100px; top: 26px;
    display: flex; align-items: center; gap: 12px; color: var(--white);
  }
  .front__brand-square { width: 44px; height: 44px; background: var(--white); border-radius: 4px; }
  .front__brand .wordmark__name { display: block; font-size: 38px; }
  .front__brand .wordmark__tag { display: block; font-size: 10.5px; letter-spacing: 1px; margin-top: 3px; text-transform: uppercase; }
  .front__person { position: absolute; left: 110px; top: 134px; }
  .front__name { color: var(--green); font-weight: 500; font-size: 21px; }
  .front__role { color: var(--muted); font-size: 14px; margin-top: 2px; }
  .front__contacts { position: absolute; left: 110px; top: 206px; list-style: none; }
  .front__contacts li {
    display: flex; align-items: center; gap: 10px;
    color: var(--muted); font-size: 14px; height: 22px;
  }
  .front__contacts svg { width: 13px; height: 13px; fill: var(--green); flex: none; }
  .front__address {
    position: absolute; right: 34px; top: 140px;
    color: var(--muted); font-size: 14px; line-height: 1.35; text-align: right; font-style: normal;
  }
</style>
</head>
<body>
  <section class="card card--back" aria-label="Card back">
    <p class="back__url">corvanebookkeeping.com</p>
    <div class="back__mark" aria-hidden="true"></div>
    <div class="wordmark back__wordmark">
      <span class="wordmark__name">Corvane</span>
      <span class="wordmark__tag">Bookkeeping Services</span>
    </div>
  </section>

  <section class="card card--front" aria-label="Card front">
    <div class="front__band"></div>
    <div class="front__rule"></div>
    <div class="front__mark" aria-hidden="true"></div>
    <div class="front__brand">
      <span class="front__brand-square" aria-hidden="true"></span>
      <div class="wordmark">
        <span class="wordmark__name">Corvane</span>
        <span class="wordmark__tag">Bookkeeping Services</span>
      </div>
    </div>
    <div class="front__person">
      <p class="front__name">Lorcan Abbey</p>
      <p class="front__role">Managing Director</p>
    </div>
    <ul class="front__contacts">
      <li><svg viewBox="0 0 16 16"><path d="M3 1h3l1.5 4-2 1.3a9 9 0 0 0 4.2 4.2L11 8.5l4 1.5v3a2 2 0 0 1-2 2A12 12 0 0 1 1 3a2 2 0 0 1 2-2z"/></svg>555-014-2278</li>
      <li><svg viewBox="0 0 16 16"><path d="M1 3h14v10H1z M2 4l6 5 6-5" stroke="#1d1e20" stroke-width="1.3"/></svg>lorcan@yourwebsite.com</li>
      <li><svg viewBox="0 0 16 16"><circle cx="8" cy="8" r="7"/><path d="M1 8h14M8 1c-3 4-3 10 0 14M8 1c3 4 3 10 0 14" stroke="#1d1e20" stroke-width="1" fill="none"/></svg>www.yourwebsite.com</li>
    </ul>
    <address class="front__address">234 Anywhere St., Any City,<br>Any Town, US 123456</address>
  </section>
</body>
</html>
```